cookie box packaging sleeve design

Hi,
I'm looking to create 5 sleeves for cookies in a box.
Classic look, not too many colors. I need to be able to add the nutrition info for each sleeve at the back.
width 110 mm height 370mm

1. Salted Tahini Choc-Chip Cookie
2. Brownie White Choc Cookie
3. Peanut Butter Cookie
4. Earthquake Cookie
5.Pistachio Cookie

ideas:
Biscotti by Brellanti (https://ryde.brellanti.example/?welcomed)
OR
https://au.snapvorra.example/pin/4830195726104388/

Target Market(s)

Family, office and for gifts

Industry/Entity Type

Cafe/Bakery

Colors

Designer to choose colors to be used in the design.

Requirements
Should not have
• Too many colours and the photo of the cookies

```html
<!DOCTYPE html>
<html lang="en">
<head>
<meta charset="utf-8">
<title>Oakridge Bakery – Cookie Sleeves</title>
<link rel="stylesheet" href="https://fonts.googleapis.com/css2?family=Baloo+2:wght@800&family=Montserrat:wght@400;700&display=swap">
<style>
  :root {
    --page: #ffffff;
    --ink: #111111;
    --white: #ffffff;
    --pb-bg: #e6ac22;  --pb-splash: #6b4a1c;
    --pb-photo-a: #b97a3c; --pb-photo-b: #8a5426;
    --eq-bg: #2e2c2d;  --eq-splash: #cf9a9b;
    --eq-photo-a: #e9e7e8; --eq-photo-b: #4a2e26;
    --th-bg: #4a8fbf;  --th-splash: #0c1a55;
    --th-photo-a: #c9a36e; --th-photo-b: #3c2416;
    --pi-bg: #a3c66a;  --pi-splash: #4c7a1d;
    --pi-photo-a: #c7a970; --pi-photo-b: #7f8a3a;
    --br-bg: #c8721e;  --br-splash: #4a2410;
    --br-photo-a: #5a3322; --br-photo-b: #2c170e;
  }
  * { box-sizing: border-box; margin: 0; padding: 0; }
  html, body { width: 1200px; height: 1200px; overflow: hidden; background: var(--page); }
  .canvas { position: relative; width: 1200px; height: 1200px; }

  .sleeve {
    position: absolute; width: 240px; height: 414px; overflow: hidden;
    background: var(--bg); box-shadow: 0 6px 18px rgba(0,0,0,.12);
  }
  .sleeve--pb { left: 133px; top: 30px;  --bg: var(--pb-bg); --splash: var(--pb-splash); --pa: var(--pb-photo-a); --pbb: var(--pb-photo-b); }
  .sleeve--eq { left: 839px; top: 30px;  --bg: var(--eq-bg); --splash: var(--eq-splash); --pa: var(--eq-photo-a); --pbb: var(--eq-photo-b); }
  .sleeve--th { left: 490px; top: 309px; --bg: var(--th-bg); --splash: var(--th-splash); --pa: var(--th-photo-a); --pbb: var(--th-photo-b); }
  .sleeve--pi { left: 171px; top: 699px; --bg: var(--pi-bg); --splash: var(--pi-splash); --pa: var(--pi-photo-a); --pbb: var(--pi-photo-b); }
  .sleeve--br { left: 826px; top: 697px; --bg: var(--br-bg); --splash: var(--br-splash); --pa: var(--br-photo-a); --pbb: var(--br-photo-b); }

  .brand {
    position: absolute; top: 52px; left: 0; right: 0; text-align: center;
    font-family: "Baloo 2", system-ui, sans-serif; font-weight: 800;
    font-size: 24px; line-height: 1; color: var(--ink);
  }

  .splash {
    position: absolute; left: 16px; right: 16px; top: 96px; height: 160px;
    background: var(--splash); border-radius: 46px;
    display: flex; flex-direction: column; align-items: center; justify-content: center;
    text-align: center; color: var(--white);
  }
  .flavour {
    font-family: "Baloo 2", system-ui, sans-serif; font-weight: 800;
    font-size: 42px; line-height: .95;
  }
  .kind {
    font-family: "Montserrat", Arial, sans-serif; font-weight: 400;
    font-size: 17px; line-height: 1.1; margin-top: 2px;
  }

  .cookie-photo {
    position: absolute; left: 0; right: 0; top: 266px; bottom: 0;
    border-radius: 50% 50% 0 0 / 22% 22% 0 0;
    background: radial-gradient(circle at 45% 45%, var(--pa), var(--pbb));
  }

  .net-weight {
    position: absolute; bottom: 0; left: 50%; transform: translateX(-50%);
    background: var(--ink); color: var(--white); white-space: nowrap;
    font-family: "Montserrat", Arial, sans-serif; font-weight: 700;
    font-size: 12px; padding: 5px 10px;
  }
</style>
</head>
<body>
<main class="canvas">

  <section class="sleeve sleeve--pb">
    <p class="brand">Oakridge Bakery</p>
    <div class="splash"><h2 class="flavour">Peanut<br>Butter</h2><p class="kind">Cookie</p></div>
    <div class="cookie-photo" role="img" aria-label="Photo of a peanut butter cookie with fork marks"></div>
    <p class="net-weight">NET WT 12OZ (340G)</p>
  </section>

  <section class="sleeve sleeve--eq">
    <p class="brand">Oakridge Bakery</p>
    <div class="splash"><h2 class="flavour">Earth<br>quake</h2><p class="kind">Cookie</p></div>
    <div class="cookie-photo" role="img" aria-label="Photo of a cracked chocolate crinkle cookie dusted with icing sugar"></div>
    <p class="net-weight">NET WT 12OZ (340G)</p>
  </section>

  <section class="sleeve sleeve--th">
    <p class="brand">Oakridge Bakery</p>
    <div class="splash"><h2 class="flavour">Salted<br>Tahini</h2><p class="kind">Choc-Chip Cookie</p></div>
    <div class="cookie-photo" role="img" aria-label="Photo of a salted tahini chocolate chip cookie"></div>
    <p class="net-weight">NET WT 12OZ (340G)</p>
  </section>

  <section class="sleeve sleeve--pi">
    <p class="brand">Oakridge Bakery</p>
    <div class="splash"><h2 class="flavour">Pistachio<br>Cookie</h2></div>
    <div class="cookie-photo" role="img" aria-label="Photo of a pistachio cookie broken open with pistachio cream"></div>
    <p class="net-weight">NET WT 12OZ (340G)</p>
  </section>

  <section class="sleeve sleeve--br">
    <p class="brand">Oakridge Bakery</p>
    <div class="splash"><h2 class="flavour">Brownie<br>White</h2><p class="kind">Choc Cookie</p></div>
    <div class="cookie-photo" role="img" aria-label="Photo of a dark brownie cookie with white chocolate chips"></div>
    <p class="net-weight">NET WT 12OZ (340G)</p>
  </section>

</main>
</body>
</html>
```